Logo with Stationery Design Project-

The company is an on-line service for assisting the people that are in a foreclosure situation with their homes. We are presently building the site on WebPelican with Wordpress.

The best option to save a home in the USA at the end of the line with the banks is to file for bankruptcy Chapter 7 or Chapter 13. We work with homeowners and attorneys to prepare the financial package for the attorneys to negotiate with the banks after filing for bankruptcy. We also sell a binder on-line which is called the keystone relief set and the web site is: www.keystonereliefset-example.com
We need a logo and stationnary to communicate the message of advisors in the field of financial strategies when it comes to the foreclosure and bankruptcy process. This stationnary will be printed on high quality paper with the business cards being on 100 stock which is high quality in the USA.

We would like to see the logo to use the Navy blue and Aqua Green colors. The final desing should communicate the financial knowledge and promise of a light at the end of the tunnell.

The card should use both sides with the back side being the logo and the web site address that links with the front of the card. Letterhead and envelopes should be serious but sexy!

A challenge that I am sure someone is up to........

Target Market(s)

12 million people that are in foreclosure in the USA and all of the law firms that deal with foreclosure and bankruptcies in the USA all 50 states

Industry/Entity Type

Financial

Requirements
Must have
• Colors are important = Navy blue and Aqua green

```html
<!DOCTYPE html>
<html lang="en">
<head>
<meta charset="utf-8">
<title>Keystone Relief Set — Stationery</title>
<link rel="stylesheet" href="https://fonts.googleapis.com/css2?family=Cabin:wght@400;500&display=swap">
<style>
  :root {
    --navy: #0a1fd6;
    --aqua: #22ffa0;
    --teal: #1d9cc4;
    --link: #1d22c9;
    --ink: #1e1e1e;
    --rule: #8a8a8a;
    --shadow: #6f6f6f;
    --paper: #ffffff;
  }
  * { box-sizing: border-box; margin: 0; padding: 0; }
  html, body { width: 921px; height: 1200px; overflow: hidden; background: var(--paper); }
  body { position: relative; font-family: "Cabin", "Gill Sans", sans-serif; color: var(--ink); }

  .sheet {
    position: absolute; left: 29px; top: 40px; width: 849px; height: 1100px;
    background: var(--paper); border: 1px solid var(--rule);
    box-shadow: 4px 4px 0 var(--shadow);
  }
  .band { position: absolute; left: 0; width: 100%; }
  .band--navy { background: var(--navy); }
  .band--aqua { background: var(--aqua); }

  .brand { position: absolute; text-align: center; color: var(--teal); font-weight: 400; letter-spacing: 0.06em; line-height: 1.2; }
  .brand__dot { display: block; margin: 0 auto; border-radius: 50%; background: var(--navy); }

  .brand--letterhead { left: 321px; top: 44px; width: 200px; font-size: 21px; }
  .brand--letterhead .brand__dot { width: 100px; height: 100px; margin-bottom: 8px; }

  .brand--envelope { left: 17px; top: 756px; width: 140px; font-size: 14px; }
  .brand--envelope .brand__dot { width: 64px; height: 64px; margin-bottom: 6px; }

  .envelope-flap { position: absolute; left: 0; top: 549px; width: 849px; height: 182px; }

  .card {
    position: absolute; width: 335px; height: 217px; background: var(--paper);
    border: 1px solid #9a9a9a; text-align: center;
  }
  .card--front { left: 107px; top: 308px; }
  .card--back { left: 412px; top: 419px; }
  .card .band--navy.top { top: 0; height: 8px; }
  .card .band--aqua.top { top: 8px; height: 7px; }
  .card .band--aqua.bottom { bottom: 9px; height: 8px; }
  .card .band--navy.bottom { bottom: 0; height: 9px; }

  .contact__name { position: absolute; top: 33px; width: 100%; font-size: 13.5px; letter-spacing: 0.04em; }
  .contact__role { position: absolute; top: 51px; width: 100%; font-size: 8px; letter-spacing: 0.04em; }
  .contact__cell { position: absolute; top: 79px; width: 100%; font-size: 11px; }
  .contact__address { position: absolute; top: 111px; width: 100%; font-size: 11.5px; line-height: 17px; }
  .contact__lines { position: absolute; top: 153px; width: 100%; font-size: 11px; line-height: 17px; }

  .brand--card { left: 92px; top: 36px; width: 150px; font-size: 13.5px; }
  .brand--card .brand__dot { width: 64px; height: 64px; margin-bottom: 4px; }
  .card__web { position: absolute; top: 157px; width: 100%; font-size: 12.5px; color: var(--link); }

  .footer {
    position: absolute; left: 0; top: 1037px; width: 100%; height: 51px;
    background: var(--aqua); color: var(--paper); text-align: center;
  }
  .footer__address { padding-top: 7px; font-size: 12px; letter-spacing: 0.1em; }
  .footer__lines { margin-top: 4px; font-size: 11px; }
</style>
</head>
<body>
  <main class="sheet">
    <div class="band band--navy" style="top:0;height:12px"></div>
    <div class="band band--aqua" style="top:12px;height:11px"></div>

    <div class="brand brand--letterhead">
      <span class="brand__dot"></span>
      KEYSTONE<br>RELIEF SET
    </div>

    <svg class="envelope-flap" viewBox="0 0 849 182" aria-hidden="true">
      <line x1="0" y1="1" x2="849" y2="1" stroke="#8a8a8a" stroke-width="1"/>
      <polyline points="0,1 424,179 849,1" fill="none" stroke="#8a8a8a" stroke-width="1"/>
    </svg>

    <section class="card card--front">
      <div class="band band--navy top"></div>
      <div class="band band--aqua top"></div>
      <p class="contact__name">MARA QUILL</p>
      <p class="contact__role">MANAGING DIRECTOR</p>
      <p class="contact__cell">CELL: 12345 6789 1033</p>
      <p class="contact__address">COMPANY NAME • 123 STREET NAME<br>AREA OF STATE • ZIP CODE • USA</p>
      <p class="contact__lines">Telephone: 123 456 7890 • Fax: 123 456 7890<br>email: sales@keystonereliefset-example.com</p>
      <div class="band band--aqua bottom"></div>
      <div class="band band--navy bottom"></div>
    </section>

    <section class="card card--back">
      <div class="band band--navy top"></div>
      <div class="band band--aqua top"></div>
      <div class="brand brand--card">
        <span class="brand__dot"></span>
        KEYSTONE<br>RELIEF SET
      </div>
      <p class="card__web">www.keystonereliefset-example.com</p>
      <div class="band band--aqua bottom"></div>
      <div class="band band--navy bottom"></div>
    </section>

    <div class="brand brand--envelope">
      <span class="brand__dot"></span>
      KEYSTONE<br>RELIEF SET
    </div>

    <div class="band band--navy" style="top:880px;height:12px"></div>
    <div class="band band--aqua" style="top:892px;height:12px"></div>

    <footer class="footer">
      <p class="footer__address">COMPANY NAME • 123 STREET NAME • AREA OF STATE • ZIP CODE • USA</p>
      <p class="footer__lines">Telephone: 123 456 7890 • Fax: 123 456 7890 • email: sales@keystonereliefset-example.com • www.keystonereliefset-example.com</p>
    </footer>
    <div class="band band--navy" style="top:1088px;height:11px"></div>
  </main>
</body>
</html>
```